Pool Screen Enclosure Building a Career Boot Camp!

Looking to Host a Boot Camp for people looking for a career or looking to change careers. We Design, Manufacture and Install Custom Pool Screen Enclosures. We have a training program to allow Non Experienced motivated people the chance at a great career that will provide a great living for them and their family. This will be a paid boot camp, week long, we provide all the initial training for them to make a transition into our business. This will be 5 days of training with a guaranteed job to start the following Monday.... This is good for both someone with no construction experience or someone with construction experience that wants to upgrade their current job.
Paid Boot Camp
transition to a full time job with great pay
Benefits include Health Insurance, Dental and Vision, 401K, we provide the tools and training.

```html
<!DOCTYPE html>
<html lang="en">
<head>
<meta charset="utf-8">
<title>Career Boot Camp Flyer</title>
<link rel="stylesheet" href="https://fonts.googleapis.com/css2?family=Oswald:wght@400;500&family=Open+Sans:wght@400;600;700&display=swap">
<style>
  :root{
    --green:#18a84a;
    --green-light:#5cbf3a;
    --yellow:#f2c230;
    --yellow-bright:#f7e03a;
    --ink:#2c2c2c;
    --white:#ffffff;
    --page:#ecebe8;
    --photo-sky:#7d8c99;
    --photo-pool:#3f6b78;
  }
  *{margin:0;padding:0;box-sizing:border-box}
  html,body{width:1200px;height:875px;overflow:hidden;background:var(--page)}
  .flyer{
    position:absolute;left:283px;top:27px;width:634px;height:820px;
    background:linear-gradient(160deg,#ffffff 40%,#eeeeee 100%);
    overflow:hidden;box-shadow:0 4px 14px rgba(0,0,0,.18);
    font-family:"Open Sans",sans-serif;color:var(--ink);
  }
  .flyer__art{position:absolute;inset:0}
  .ribbon-text{
    position:absolute;left:450px;top:70px;width:200px;height:28px;line-height:28px;text-align:center;
    transform:rotate(45deg);font-family:"Oswald",sans-serif;font-weight:500;
    font-size:21px;color:var(--white);letter-spacing:.2px;white-space:nowrap;
  }
  .hero-title{position:absolute;left:21px;top:350px;font-family:"Oswald",sans-serif;font-weight:500;line-height:1;white-space:nowrap}
  .hero-title__main{display:block;font-size:33px;color:var(--white);transform:scaleX(.78);transform-origin:left}
  .hero-title__sub{display:block;margin-top:8px;font-size:28px;color:var(--yellow-bright);transform:scaleX(.8);transform-origin:left}
  .paid-badge{
    position:absolute;left:473px;top:440px;width:104px;height:104px;border-radius:50%;
    background:var(--yellow);color:var(--white);font-family:"Oswald",sans-serif;font-weight:500;
    font-size:20px;line-height:1.15;display:flex;flex-direction:column;align-items:center;justify-content:center;
  }
  .section{position:absolute;left:24px}
  .section--career{top:512px}
  .section--bootcamp{top:612px}
  .section__title{font-family:"Oswald",sans-serif;font-weight:500;font-size:27px;color:var(--green);line-height:1.1;transform:scaleX(.84);transform-origin:left;white-space:nowrap}
  .section__list{list-style:none;margin-top:4px}
  .section__list li{position:relative;padding-left:23px;line-height:19px;white-space:nowrap}
  .section__list li::before{
    content:"›";position:absolute;left:3px;top:5px;width:10px;height:10px;border-radius:50%;
    background:var(--ink);color:var(--white);font-size:10px;line-height:8px;text-align:center;font-weight:700;
  }
  .section--career li{font-size:13.5px;text-transform:uppercase;letter-spacing:.2px}
  .section--bootcamp li{font-size:12px}
  .brand{position:absolute;left:28px;top:718px;display:flex;align-items:center;gap:8px}
  .brand__dot{width:24px;height:24px;border-radius:50%;background:var(--green)}
  .brand__name{font-family:"Open Sans",sans-serif;font-weight:700;font-size:19px;color:var(--ink);line-height:1}
  .brand__tag{position:absolute;left:60px;top:743px;font-size:11.5px;font-weight:600;color:var(--ink)}
  .contact{position:absolute;right:28px;top:752px;text-align:right;color:var(--white);font-size:15px;line-height:19px;font-style:normal}
  .contact__phone{display:inline-flex;align-items:center;gap:4px}
  .contact__icon{width:14px;height:14px}
</style>
</head>
<body>
<article class="flyer">
  <svg class="flyer__art" width="634" height="820" viewBox="0 0 634 820">
    <defs>
      <linearGradient id="heroPhoto" x1="0" y1="0" x2="0" y2="1">
        <stop offset="0" stop-color="#5a6672"/>
        <stop offset=".45" stop-color="#7d8c99"/>
        <stop offset=".75" stop-color="#3f6b78"/>
        <stop offset="1" stop-color="#8a7d63"/>
      </linearGradient>
      <linearGradient id="circleSky" x1="0" y1="0" x2="0" y2="1">
        <stop offset="0" stop-color="#6f8db0"/>
        <stop offset="1" stop-color="#a9b4ae"/>
      </linearGradient>
      <linearGradient id="circleSand" x1="0" y1="0" x2="1" y2="1">
        <stop offset="0" stop-color="#b18a6f"/>
        <stop offset="1" stop-color="#d8d2c4"/>
      </linearGradient>
      <linearGradient id="footGreen" x1="0" y1="0" x2="1" y2="0">
        <stop offset="0" stop-color="#5cbf3a"/>
        <stop offset="1" stop-color="#18a84a"/>
      </linearGradient>
    </defs>

    <rect class="hero-photo" x="0" y="0" width="634" height="360" fill="url(#heroPhoto)" role="img" aria-label="Photo of a worker in a plaid shirt and tool belt in front of a screened pool enclosure"/>

    <polygon class="corner-ribbon" points="438,0 494,0 634,140 634,196" fill="var(--yellow)"/>

    <path class="hero-swoosh-edge" d="M0,335 C110,300 250,295 350,350 L350,460 C250,520 110,520 0,480 Z" fill="var(--yellow)"/>
    <path class="hero-swoosh" d="M0,330 C110,292 250,288 350,342 L350,450 C250,505 110,505 0,468 Z" fill="var(--green)"/>

    <g class="work-photos">
      <circle cx="424" cy="290" r="85" fill="var(--white)" stroke="var(--green-light)" stroke-width="3"/>
      <circle cx="424" cy="290" r="79" fill="url(#circleSky)" role="img" aria-label="Photo of two installers fitting a screen frame"/>
      <circle cx="402" cy="450" r="68" fill="var(--white)" stroke="var(--green-light)" stroke-width="3"/>
      <circle cx="402" cy="450" r="62" fill="url(#circleSand)" role="img" aria-label="Photo of workers reviewing enclosure plans"/>
      <circle cx="533" cy="382" r="104" fill="var(--white)" stroke="var(--green-light)" stroke-width="3"/>
      <circle cx="533" cy="382" r="97" fill="url(#circleSky)" role="img" aria-label="Photo of an installer on a ladder inside an enclosure frame"/>
    </g>

    <path class="foot-swoosh-edge" d="M0,738 C140,800 330,720 634,700 L634,716 C330,740 140,820 0,760 Z" fill="var(--yellow)"/>
    <path class="foot-band" d="M0,772 C150,820 330,748 634,724 L634,820 L0,820 Z" fill="url(#footGreen)"/>
  </svg>

  <div class="ribbon-text">CAREER BOOT CAMP!</div>

  <h1 class="hero-title">
    <span class="hero-title__main">POOL SCREEN ENCLOSURE</span>
    <span class="hero-title__sub">BUILDING A CAREER BOOT CAMP!</span>
  </h1>

  <div class="paid-badge"><span>$ PAID $</span><span>BOOT CAMP</span></div>

  <section class="section section--career">
    <h2 class="section__title">CAREER IN POOL SCREEN ENCLOSURES</h2>
    <ul class="section__list">
      <li>Transition to a <strong>full time job with great pay</strong></li>
      <li>Benefits include <strong>health insurance, dental and vision, 401K</strong></li>
      <li><strong>We provide the tools and training</strong></li>
    </ul>
  </section>

  <section class="section section--bootcamp">
    <h2 class="section__title">PAID BOOT CAMP</h2>
    <ul class="section__list">
      <li>Paid boot camp one week long</li>
      <li>We provide all the initial training for you to make a transition into our business.</li>
      <li>This will be 5 days of training with a <strong>GUARANTEED JOB</strong> to start the following Monday.</li>
    </ul>
  </section>

  <div class="brand">
    <span class="brand__dot"></span>
    <span class="brand__name">Lanai Craft Co.</span>
  </div>
  <div class="brand__tag">Built for Life Outdoors</div>

  <address class="contact">
    <div>Contact Us <span class="contact__phone"><svg class="contact__icon" viewBox="0 0 16 16"><circle cx="8" cy="8" r="7" fill="none" stroke="#fff" stroke-width="1.4"/><path d="M5.5,4.5 L7,4.2 L7.6,6 L6.8,6.8 C7.2,7.8 8.2,8.8 9.2,9.2 L10,8.4 L11.8,9 L11.5,10.5 C8.5,11 5,7.5 5.5,4.5 Z" fill="#fff"/></svg>555-014-2290</span></div>
    <div>hello@lanaicraftco.com</div>
    <div>418 Harbor Palm Avenue, Port Sable FL 34990</div>
  </address>
</article>
</body>
</html>
```